International Sex Coach needs a Book Cover in less than 3 days

I need a cover design for my book coming out next week titled "A Quiet Atlas Toward Closeness". The book explores the origins of our cultural ideas about sexuality and taboo and is interwoven with personal memoir.
The reader must feel that they are being pulled into an intimate sexual story, but also a deeper understanding of sex itself. Like they are jumping into bed with me, you might say. I would like the title to take up the majority of the space over an image of 3D, very real bed sheets, but I am open to your ideas. I haven't purchased any images yet, but there are a few below I was drawn to.
In its essence, this book is designed to reeducate the reader about sexuality and open them up to a new paradigm of sexual wellness.
The author name is Mirela Oswin. Page must also include the phrase: a revolutionary new approach to sexuality, relationship and love.
Size 6" x 9" (15.24 x 22.86 cm)
Thanks!

Reason: I need more time to review the designs and give feedback.

Target Market(s)

Sexually active men and women.

Industry/Entity Type

Wellness

Font styles to use
Serif

```html
<!DOCTYPE html>
<html lang="en">
<head>
<meta charset="utf-8">
<title>A Quiet Atlas Toward Closeness — Mirela Oswin</title>
<link rel="stylesheet" href="https://fonts.googleapis.com/css2?family=Josefin+Sans:wght@300;400&family=Montserrat:wght@800&family=Great+Vibes&display=swap">
<style>
  :root {
    --sheet-light: #e6e6e6;
    --sheet-mid: #b9b9b9;
    --sheet-dark: #8c8c8c;
    --band-deep: rgba(128, 22, 22, 0.92);
    --band-soft: rgba(196, 96, 96, 0.85);
    --cream: #efe9d2;
    --ink: #0d0d0d;
    --crimson: #9a1638;
  }
  html, body {
    margin: 0;
    padding: 0;
    width: 800px;
    height: 1200px;
    overflow: hidden;
    background: #ffffff;
  }
  .cover {
    position: relative;
    width: 800px;
    height: 1200px;
    overflow: hidden;
  }
  .cover-photo {
    position: absolute;
    inset: 0;
    background:
      radial-gradient(ellipse at 45% 30%, var(--sheet-mid) 0%, transparent 45%),
      radial-gradient(ellipse at 30% 80%, var(--sheet-light) 0%, transparent 55%),
      linear-gradient(160deg, var(--sheet-light) 0%, var(--sheet-mid) 45%, var(--sheet-light) 70%, var(--sheet-dark) 100%);
  }
  .cover-type {
    position: absolute;
    inset: 0;
  }
  .author-band { fill: url(#bandFade); }
  .author-name {
    font-family: "Josefin Sans", sans-serif;
    font-weight: 300;
    font-size: 74px;
    fill: var(--cream);
  }
  .title-script {
    font-family: "Great Vibes", cursive;
    font-size: 112px;
    fill: var(--ink);
  }
  .title-bold {
    font-family: "Montserrat", sans-serif;
    font-weight: 800;
    font-size: 208px;
    fill: var(--ink);
  }
  .title-small {
    font-family: "Josefin Sans", sans-serif;
    font-weight: 400;
    font-size: 52px;
    fill: var(--ink);
  }
  .title-accent {
    font-family: "Josefin Sans", sans-serif;
    font-weight: 300;
    font-size: 190px;
    fill: var(--crimson);
  }
  .tagline {
    font-family: "Josefin Sans", sans-serif;
    font-weight: 400;
    font-size: 28px;
    letter-spacing: 1px;
    fill: var(--ink);
  }
</style>
</head>
<body>
<main class="cover">
  <div class="cover-photo" role="img" aria-label="Black and white photograph of a woman lying among soft, rumpled satin bed sheets"></div>
  <svg class="cover-type" width="800" height="1200" viewBox="0 0 800 1200" xmlns="http://www.w3.org/2000/svg">
    <defs>
      <linearGradient id="bandFade" x1="0" y1="0" x2="1" y2="0">
        <stop offset="0" stop-color="var(--band-deep)"/>
        <stop offset="0.55" stop-color="var(--band-deep)"/>
        <stop offset="1" stop-color="var(--band-soft)"/>
      </linearGradient>
    </defs>
    <rect class="author-band" x="0" y="42" width="800" height="96"/>
    <text class="author-name" x="400" y="118" text-anchor="middle" textLength="520" lengthAdjust="spacingAndGlyphs">Mirela Oswin</text>

    <text class="title-script" x="84" y="466" textLength="420" lengthAdjust="spacingAndGlyphs">A Quiet</text>
    <text class="title-bold" x="100" y="696" textLength="632" lengthAdjust="spacingAndGlyphs">ATLAS</text>
    <text class="title-small" x="96" y="790">toward</text>
    <text class="title-accent" x="80" y="985" textLength="660" lengthAdjust="spacingAndGlyphs">CLOSENESS</text>

    <text class="tagline" x="400" y="1082" text-anchor="middle">a revolutionary new approach to</text>
    <text class="tagline" x="400" y="1120" text-anchor="middle">sexuality, relationship and love</text>
  </svg>
</main>
</body>
</html>
```